Digital Signage Design Project

Our company sells digital signage systems. I want some images created explaining the benefits of the software we sell. These will be a series of slide backgrounds in .PSD format with all layers accessible. I imagine approximately 10 slides at 1920 x 1080 and the same design done again in portrait (1080 x 1920). They need to look modern and professional but be eye-catching. They will involve both text and graphics. The copy will be supplied but some of the graphic images will need to be created.
The software is called VORTIQ7 and logos are attached. You can find out more about VORTIQ7 at this link...
http://www.klr-example.eu/pages/home.aspx
Target Market(s)
Business
Industry/Entity Type
Software
Look and feel
Each slider illustrates characteristics of the customer's brand and the style your logo design should communicate.

```html
<!DOCTYPE html>
<html lang="en">
<head>
<meta charset="utf-8">
<title>Got Something to Say? – VORTIQ7</title>
<link href="https://fonts.googleapis.com/css2?family=Open+Sans:wght@300;400;700&display=swap" rel="stylesheet">
<style>
  :root {
    --top-strip: #9e2408;
    --ember: #b3300c;
    --deep-ember: #8f1f06;
    --flame: #f2650f;
    --bright-flame: #ff7a14;
    --glow: #ffd866;
    --amber: #f7a228;
    --band: #ffffff;
    --ink: #0e0e0e;
    --brand-ink: #2f2f2f;
    --line-light: rgba(255, 236, 190, 0.35);
    --line-faint: rgba(255, 236, 190, 0.18);
  }
  html, body {
    margin: 0;
    padding: 0;
    overflow: hidden;
    background: #ffffff;
  }
  .slide {
    position: relative;
    width: 1200px;
    height: 675px;
    overflow: hidden;
    font-family: "Open Sans", sans-serif;
  }
  .slide__backdrop {
    position: absolute;
    inset: 0;
    background:
      radial-gradient(ellipse 330px 260px at 330px 330px, rgba(255, 226, 120, 0.95), rgba(255, 210, 100, 0) 72%),
      radial-gradient(ellipse 300px 380px at 620px 470px, rgba(255, 190, 70, 0.75), rgba(255, 190, 70, 0) 75%),
      radial-gradient(ellipse 460px 300px at 470px 250px, rgba(250, 170, 50, 0.8), rgba(250, 170, 50, 0) 75%),
      radial-gradient(ellipse 420px 520px at 1120px 430px, rgba(255, 122, 20, 0.95), rgba(255, 122, 20, 0) 80%),
      radial-gradient(ellipse 260px 420px at 40px 520px, rgba(143, 31, 6, 0.85), rgba(143, 31, 6, 0) 80%),
      linear-gradient(180deg, var(--top-strip) 0%, var(--ember) 22%, var(--flame) 60%, #d2470f 100%);
  }
  .slide__arcs {
    position: absolute;
    inset: 0;
    width: 1200px;
    height: 675px;
  }
  .arc {
    fill: none;
    stroke-width: 1.5;
  }
  .arc--light { stroke: var(--line-light); }
  .arc--faint { stroke: var(--line-faint); }
  .sweep { fill: rgba(255, 225, 150, 0.14); }
  .title-band {
    position: absolute;
    left: 0;
    top: 47px;
    width: 100%;
    height: 93px;
    background: var(--band);
  }
  .title-band__heading {
    position: absolute;
    left: 79px;
    top: 11px;
    margin: 0;
    font-size: 53px;
    line-height: 72px;
    font-weight: 300;
    color: var(--ink);
    letter-spacing: -0.8px;
    white-space: nowrap;
  }
  .title-band__heading strong {
    font-weight: 700;
  }
  .brand {
    position: absolute;
    right: 22px;
    top: 47px;
    height: 93px;
    display: flex;
    align-items: center;
    gap: 10px;
  }
  .brand__mark {
    width: 14px;
    height: 14px;
    background: var(--flame);
  }
  .brand__name {
    font-size: 40px;
    font-weight: 700;
    color: var(--brand-ink);
    letter-spacing: 1px;
  }
</style>
</head>
<body>
  <main class="slide">
    <div class="slide__backdrop" role="img" aria-label="Warm orange photo collage of a surgeon in cap and goggles looking at translucent medical display screens"></div>
    <svg class="slide__arcs" viewBox="0 0 1200 675" aria-hidden="true">
      <path class="sweep" d="M0 600 C 260 420, 560 330, 1200 380 L 1200 430 C 560 390, 280 470, 0 660 Z"/>
      <path class="arc arc--light" d="M0 250 C 300 180, 700 230, 1200 180"/>
      <path class="arc arc--faint" d="M60 675 C 180 420, 420 250, 760 140"/>
      <path class="arc arc--light" d="M380 675 C 420 470, 560 300, 820 140"/>
      <path class="arc arc--faint" d="M720 0 C 860 200, 900 420, 820 675"/>
      <path class="arc arc--faint" d="M0 420 C 380 380, 800 440, 1200 520"/>
      <path class="arc arc--light" d="M520 675 C 700 520, 940 440, 1200 410"/>
    </svg>
    <header class="title-band">
      <h1 class="title-band__heading"><strong>Got Something</strong> to Say?</h1>
    </header>
    <div class="brand">
      <span class="brand__mark" aria-hidden="true"></span>
      <span class="brand__name">VORTIQ7</span>
    </div>
  </main>
</body>
</html>
```